I need a simple, classy and stylish business card. I would like it to have a black background with white writing. I would like you to use my logo you designed on the front with the word 'Imagery" used underneath it in the same font. On the back I was thinking of the website at the top 'tormavine.com' Then my social media accounts, Can you use the instagram, Facebook and twitter logo then my handles?
Please let me know what you think.
Regards Lars
Industry/Entity Type
Business
Requirements
Must have
- Website: www.tormavine.com
- Social media handles..
- Instagram: @Lars_Tormavine_Imagery
- Facebook: Lars Tormavine Imagery
- Twitter: @Lars_Tormavin
- Email: info@tormavin.com
- Phone: 0473 518 609

```html
<!DOCTYPE html>
<html lang="en">
<head>
<meta charset="utf-8">
<title>Lars Tormavine Imagery – Business Card</title>
<link rel="stylesheet" href="https://fonts.googleapis.com/css2?family=Open+Sans:wght@300;400;700&display=swap">
<style>
  :root {
    --ink: #000000;
    --paper: #ffffff;
    --rule: #8a8a8a;
    --stage: #ececec;
  }
  * { margin: 0; padding: 0; box-sizing: border-box; }
  html, body {
    width: 1200px;
    height: 900px;
    overflow: hidden;
    background: var(--stage);
    font-family: "Open Sans", sans-serif;
  }
  .canvas { position: relative; width: 1200px; height: 900px; }

  .card {
    position: absolute;
    background: var(--ink);
    color: var(--paper);
    overflow: hidden;
    box-shadow: 0 6px 18px rgba(0,0,0,0.18);
  }
  .card-base { position: absolute; inset: 0; display: block; }

  /* Front */
  .card--front { left: 78px; top: 34px; width: 588px; height: 364px; }
  .brand-mark {
    position: absolute;
    left: 124px; top: 128px;
    width: 40px; height: 40px;
    border: 3px solid var(--paper);
    border-radius: 50%;
  }
  .brand-name {
    position: absolute;
    left: 178px; top: 138px;
    font-weight: 300;
    font-size: 38px;
    line-height: 1;
    letter-spacing: 0.5px;
    white-space: nowrap;
  }
  .brand-tagline {
    position: absolute;
    left: 128px; top: 212px;
    width: 336px;
    display: flex;
    align-items: center;
    gap: 10px;
  }
  .brand-tagline__rule { flex: 1; height: 1px; background: var(--rule); }
  .brand-tagline__word {
    font-weight: 300;
    font-size: 18px;
    line-height: 1;
  }

  /* Back */
  .card--back { left: 388px; top: 505px; width: 567px; height: 352px; }
  .social-list {
    position: absolute;
    left: 0; right: 0; top: 102px;
    list-style: none;
    display: flex;
    flex-direction: column;
    align-items: center;
    gap: 16px;
  }
  .social-list__item {
    display: flex;
    align-items: center;
    gap: 8px;
    font-size: 18px;
    line-height: 24px;
  }
  .social-list__icon {
    width: 18px; height: 18px;
    border-radius: 50%;
    background: var(--paper);
    flex: none;
  }
  .website {
    position: absolute;
    right: 30px; top: 306px;
    color: var(--ink);
    font-weight: 700;
    font-size: 18px;
    line-height: 1;
  }
</style>
</head>
<body>
<main class="canvas">

  <section class="card card--front" aria-label="Business card front">
    <svg class="card-base" width="588" height="364" viewBox="0 0 588 364" aria-hidden="true">
      <polygon fill="#ffffff" points="0,299 428,299 436,291 588,291 588,364 0,364"/>
      <polyline fill="none" stroke="#000000" stroke-width="2.5" points="0,326 392,326 424,291"/>
    </svg>
    <span class="brand-mark" aria-hidden="true"></span>
    <h1 class="brand-name">Lars Tormavine</h1>
    <div class="brand-tagline">
      <span class="brand-tagline__rule"></span>
      <span class="brand-tagline__word">Imagery</span>
      <span class="brand-tagline__rule"></span>
    </div>
  </section>

  <section class="card card--back" aria-label="Business card back">
    <svg class="card-base" width="567" height="352" viewBox="0 0 567 352" aria-hidden="true">
      <polygon fill="#ffffff" points="0,272 364,272 372,266 567,266 567,352 0,352"/>
      <polyline fill="none" stroke="#000000" stroke-width="2.5" points="0,300 345,300 374,266"/>
    </svg>
    <ul class="social-list">
      <li class="social-list__item"><span class="social-list__icon" aria-hidden="true"></span>@Lars_Tormavine_Imagery</li>
      <li class="social-list__item"><span class="social-list__icon" aria-hidden="true"></span>@LarsTormavineImagery</li>
      <li class="social-list__item"><span class="social-list__icon" aria-hidden="true"></span>@Lars_Tormavin</li>
    </ul>
    <p class="website">www.tormavine.com</p>
  </section>

</main>
</body>
</html>
```